Stationery Design Project

We are looking stationary Design for Velbrook International, a high end clothing company. I have attached an image of our Logo below.
Updates
I am looking for designs for the following stationaries:
1. Leather Binders
2. Paper Binders
3. Letterhead
4. Envelopes
5. Pens, pencils etc
We would love to see designs with gold, black and white color combination.
Industry/Entity Type
Clothing
Look and feel
Each slider illustrates characteristics of the customer's brand and the style your logo design should communicate.

```html
<!DOCTYPE html>
<html lang="en">
<head>
<meta charset="utf-8">
<title>Velbrook International — Stationery</title>
<link href="https://fonts.googleapis.com/css2?family=Arimo:wght@400;700&display=swap" rel="stylesheet">
<style>
  :root{
    --frame:#000;
    --sheet:#fff;
    --ink:#111;
    --line:#222;
    --header-band:#333;
    --stage-top:#e4edf0;
    --stage-bottom:#eef1f2;
    --crest-faint:#f1f1f1;
    --muted:#777;
  }
  *{margin:0;padding:0;box-sizing:border-box}
  html,body{width:1200px;height:669px;overflow:hidden;background:var(--frame)}
  body{font-family:"Arimo",Arial,sans-serif;color:var(--ink)}
  .board{position:absolute;left:25px;top:25px;width:1150px;height:618px;background:var(--sheet)}
  .piece{position:absolute}
  .stage{position:absolute;left:55px;width:414px}
  .stage--top{top:64px;height:276px;background:var(--stage-top)}
  .stage--bottom{top:340px;height:274px;background:var(--stage-bottom)}

  .wordmark{display:flex;flex-direction:column;align-items:center;gap:2px;font-weight:400;letter-spacing:.12em;text-transform:uppercase;color:var(--ink)}
  .wordmark__dot{width:9px;height:9px;border:1px solid currentColor;border-radius:50%}
  .wordmark__name{font-size:5px;line-height:1.1;text-align:center}
  .wordmark--light{color:#fff}

  /* paper binder */
  .paper-binder{left:172px;top:100px;width:180px;height:205px;background:#fff;border:1px solid #ccc}
  .paper-binder__band{position:absolute;left:0;right:0;top:128px;height:26px;background:var(--ink)}
  .paper-binder .wordmark{position:absolute;left:0;right:0;top:40px}
  .paper-binder .wordmark__dot{width:20px;height:20px}
  .paper-binder .wordmark__name{font-size:9px}

  /* leather binder */
  .leather-binder{left:170px;top:368px;width:184px;height:220px;background:#161616;border-left:6px solid #050505}
  .leather-binder .wordmark{position:absolute;left:0;right:0;top:40px;color:#cfcfcf}
  .leather-binder .wordmark__dot{width:30px;height:30px}
  .leather-binder .wordmark__name{font-size:11px;letter-spacing:.16em}

  .letterhead{top:61px;width:186px;height:302px;background:#fff;border:1px solid var(--line)}
  .letterhead--plain{left:511px}
  .letterhead--banded{left:745px;width:214px}
  .letterhead--plain .wordmark{position:absolute;left:0;right:0;top:8px}
  .letterhead__band{position:absolute;left:9px;right:9px;top:4px;height:28px;background:var(--header-band)}
  .letterhead__band .wordmark{margin-top:5px}
  .crest-area{position:absolute;background:var(--crest-faint);border-radius:40% 40% 45% 45%}
  .letterhead .crest-area{left:24px;width:140px;top:100px;height:170px}
  .letterhead--banded .crest-area{left:36px}

  .card{left:993px;width:161px;height:90px;background:#fff;border:1px solid var(--line)}
  .card--front{top:165px}
  .card--front .wordmark{position:absolute;left:0;right:0;top:24px}
  .card__name{position:absolute;left:0;right:0;top:56px;text-align:center;font-size:9.5px}
  .card--back{top:273px}
  .card__contact{position:absolute;left:7px;right:8px;top:47px;height:36px;background:var(--ink);color:#fff;font-size:5.6px;line-height:1.2;padding:14px 0 0 7px}

  .envelope{width:230px;height:105px;background:#fff;border:1px solid var(--line);overflow:hidden}
  .envelope svg.flap{position:absolute;inset:0}
  .envelope--front{left:495px;top:393px}
  .envelope--front .wordmark{position:absolute;left:0;right:0;top:15px}
  .envelope--back-dark{left:747px;top:393px;width:229px;background:var(--ink);border-color:var(--ink)}
  .envelope--faces{left:495px;top:510px;height:104px}
  .envelope--faces .crest-area{left:148px;top:8px;width:110px;height:130px}
  .envelope--dark{left:747px;top:510px;width:229px;height:103px;background:var(--ink);border-color:var(--ink)}
  .envelope__strip{position:absolute;left:8px;right:8px;top:69px;height:28px;background:#fff;padding-top:4px}
  .envelope__strip .wordmark__dot{background:var(--ink)}
</style>
</head>
<body>
<main class="board"></main>

<section class="stage stage--top" aria-label="Paper binder">
</section>
<div class="piece stage" style="top:64px;height:276px">
  <div class="piece paper-binder" style="left:117px;top:36px">
    <div class="wordmark"><span class="wordmark__dot"></span><span class="wordmark__name">Velbrook<br>International</span></div>
    <div class="paper-binder__band"></div>
  </div>
</div>

<section class="stage stage--bottom" aria-label="Leather binder"></section>
<div class="piece stage" style="top:340px;height:274px">
  <div class="piece leather-binder" style="left:115px;top:28px">
    <div class="wordmark"><span class="wordmark__dot"></span><span class="wordmark__name">Velbrook<br>International</span></div>
  </div>
</div>

<article class="piece letterhead letterhead--plain">
  <div class="wordmark"><span class="wordmark__dot"></span><span class="wordmark__name">Velbrook<br>International</span></div>
  <div class="crest-area" role="img" aria-label="Faint heraldic crest watermark"></div>
</article>

<article class="piece letterhead letterhead--banded">
  <div class="letterhead__band">
    <div class="wordmark wordmark--light"><span class="wordmark__dot"></span><span class="wordmark__name">Velbrook<br>International</span></div>
  </div>
  <div class="crest-area" role="img" aria-label="Faint heraldic crest watermark"></div>
</article>

<article class="piece card card--front">
  <div class="wordmark"><span class="wordmark__dot"></span><span class="wordmark__name">Velbrook<br>International</span></div>
  <p class="card__name">Clara Hensley</p>
</article>

<article class="piece card card--back">
  <div class="card__contact">
    Av. Lorne 118<br>2209 551 870 &nbsp; 099 612 407<br>clara@velbrook.com
  </div>
</article>

<article class="piece envelope envelope--front">
  <svg class="flap" width="230" height="105" viewBox="0 0 230 105"><polyline points="0,0 115,52 230,0" fill="none" stroke="#222" stroke-width="1"/></svg>
  <div class="wordmark"><span class="wordmark__dot"></span><span class="wordmark__name">Velbrook<br>International</span></div>
</article>

<article class="piece envelope envelope--back-dark">
  <svg class="flap" width="229" height="105" viewBox="0 0 229 105"><polyline points="0,0 114,52 229,0" fill="none" stroke="#fff" stroke-width="1"/></svg>
</article>

<article class="piece envelope envelope--faces">
  <div class="crest-area" role="img" aria-label="Faint heraldic crest watermark, partly cropped"></div>
</article>

<article class="piece envelope envelope--dark">
  <div class="envelope__strip">
    <div class="wordmark"><span class="wordmark__dot"></span><span class="wordmark__name">Velbrook<br>International</span></div>
  </div>
</article>
</body>
</html>
```